Construction Company

Design a clutter free business card, it can be double-sided utilizing the logo for BDN Ltd simple with all relevant contact information.

Please also a letterhead design to function for the purposes of invoicing, all mail requirements, with header to be distinctive while the footer ties page together and incorporates all necessary information.

For now, please use generic / dummy text and when a winner is selected, I will disclose the contact information.

Hi Designers! Please read the updated brief which includes the design of a business card and letterhead. Thank you!

```html
<!DOCTYPE html>
<html lang="en">
<head>
<meta charset="utf-8">
<title>BDN Ltd – Business Card</title>
<link rel="stylesheet" href="https://fonts.googleapis.com/css2?family=Tinos:wght@400;700&display=swap">
<style>
  :root {
    --navy: #263b8a;
    --gold: #b8912f;
    --white: #ffffff;
    --backdrop: #8c6d4c;
  }
  * { margin: 0; padding: 0; box-sizing: border-box; }
  html, body {
    width: 900px;
    height: 1200px;
    overflow: hidden;
  }
  body {
    position: relative;
    background: var(--backdrop);
    font-family: "Tinos", "Times New Roman", serif;
  }
  .card {
    position: absolute;
    left: 80px;
    width: 734px;
    height: 429px;
    border-radius: 30px;
    overflow: hidden;
  }
  .card--front { top: 128px; background: var(--white); }
  .card--back  { top: 645px; background: var(--navy); }

  .brand-name {
    position: absolute;
    font-weight: 400;
    letter-spacing: 1px;
    white-space: nowrap;
  }
  .card--front .brand-name {
    left: 90px;
    top: 162px;
    font-size: 76px;
    line-height: 1;
    color: var(--navy);
  }
  .card--back .brand-name {
    left: 0;
    right: 0;
    top: 160px;
    text-align: center;
    font-size: 96px;
    line-height: 1;
    color: var(--white);
  }

  .divider {
    position: absolute;
    left: 400px;
    top: 112px;
    width: 2px;
    height: 204px;
    background: var(--navy);
  }
  .contact {
    position: absolute;
    left: 436px;
    top: 104px;
    color: var(--navy);
  }
  .contact__name {
    font-size: 33px;
    font-weight: 700;
    line-height: 1;
    letter-spacing: 0.5px;
  }
  .contact__title {
    margin-top: 6px;
    font-size: 17px;
    color: var(--gold);
    letter-spacing: 0.3px;
  }
  .contact__list { list-style: none; margin-top: 14px; }
  .contact__item {
    display: flex;
    align-items: flex-start;
    font-size: 17px;
    line-height: 23px;
  }
  .contact__item + .contact__item { margin-top: 0; }
  .contact__item--address { margin-bottom: 9px; }
  .contact__icon {
    width: 14px;
    height: 14px;
    margin: 4px 10px 0 0;
    flex: none;
    fill: var(--gold);
  }
</style>
</head>
<body>
  <section class="card card--front" aria-label="Business card front">
    <div class="brand-name">BDN Ltd</div>
    <div class="divider"></div>
    <div class="contact">
      <h1 class="contact__name">DANIEL WARD</h1>
      <p class="contact__title">MANAGING DIRECTOR</p>
      <ul class="contact__list">
        <li class="contact__item contact__item--address">
          <svg class="contact__icon" viewBox="0 0 14 14" aria-hidden="true"><path d="M7 0a5 5 0 0 0-5 5c0 3.5 5 9 5 9s5-5.5 5-9a5 5 0 0 0-5-5zm0 7a2 2 0 1 1 0-4 2 2 0 0 1 0 4z"/></svg>
          <span>118 Harlow Street NW<br>Suite 210, Brookfield<br>MI 49877</span>
        </li>
        <li class="contact__item">
          <svg class="contact__icon" viewBox="0 0 14 14" aria-hidden="true"><path d="M3 0.5l2.3 2.8-1.3 1.9c.9 1.9 2.4 3.4 4.3 4.3l1.9-1.3 2.8 2.3-1.3 2.5C6.300 12.700 1.300 7.700 0.500 1.800z"/></svg>
          <span>555 210 3478</span>
        </li>
        <li class="contact__item">
          <svg class="contact__icon" viewBox="0 0 14 14" aria-hidden="true"><path d="M1 3h12v8H1z M1 3l6 4.5L13 3" stroke="#fff" stroke-width="1"/></svg>
          <span>info@bdnltd.com</span>
        </li>
        <li class="contact__item">
          <svg class="contact__icon" viewBox="0 0 14 14" aria-hidden="true"><circle cx="7" cy="7" r="6.5"/><path d="M0.5 7h13M7 0.5v13M2 3.5h10M2 10.5h10M7 0.5c-3 3.5-3 9.5 0 13M7 0.5c3 3.5 3 9.5 0 13" stroke="#fff" stroke-width="0.8" fill="none"/></svg>
          <span>www.bdnltd.com</span>
        </li>
      </ul>
    </div>
  </section>

  <section class="card card--back" aria-label="Business card back">
    <div class="brand-name">BDN Ltd</div>
  </section>
</body>
</html>
```